Velmora - 3D medical animations and high end visual content

Our company creates high end visual content and animations for medical global companies.
Our website - www.velmora-studio.example
We would like to have an amazing business card for our CEO that he can use in the following exhebitions he is going to attend.
It is very important that the design will be memorable and diffrent. It has to reflect our brand design (you can have it from our website)
We would like to transmit innovation, prestige, luxury, aesthetics.
The card has to be Double Sided

Target Market(s)

Marketing managers in medical global companys

Industry/Entity Type

It Company

Contact Information for Business Card

Requirements
Nice to have
• It is very important that the design will be memorable and diffrent. It has to reflect our brand design (you can have it from our website)

```html
<!DOCTYPE html>
<html lang="en">
<head>
<meta charset="utf-8">
<title>Velmora – Business Card</title>
<link rel="stylesheet" href="https://fonts.googleapis.com/css2?family=Saira:wght@400;500&family=Jura:wght@500&display=swap">
<style>
  :root {
    --backdrop: #bebfc1;
    --navy-deep: #08141f;
    --navy-mid: #0b2d4f;
    --blue-bright: #0562a6;
    --teal: #0a8ca3;
    --grid-line: rgba(120, 180, 230, 0.10);
    --ink: #ffffff;
  }
  * { margin: 0; padding: 0; box-sizing: border-box; }
  html, body {
    width: 1200px; height: 1200px; overflow: hidden;
    background: var(--backdrop);
  }
  .canvas { position: relative; width: 1200px; height: 1200px; }

  .card {
    position: absolute; top: 451px;
    width: 461px; height: 298px; overflow: hidden;
    background:
      linear-gradient(var(--grid-line) 1px, transparent 1px) 0 0 / 77px 77px,
      linear-gradient(90deg, var(--grid-line) 1px, transparent 1px) 0 0 / 77px 77px,
      linear-gradient(180deg, rgba(0,0,0,0) 40%, rgba(0,0,0,0.25) 100%),
      linear-gradient(100deg, var(--navy-deep) 0%, var(--navy-mid) 42%, var(--blue-bright) 100%);
    color: var(--ink);
  }
  .card--front { left: 94px; }
  .card--back { left: 664px; }

  .band { position: absolute; background: var(--teal); width: 38px; }
  .card--front .band { left: 126px; }
  .card--front .band--top { top: 0; height: 80px; }
  .card--front .band--bottom { top: 138px; bottom: 0; }

  .brand-name {
    position: absolute; left: 40px; top: 82px; width: 382px;
    font-family: "Saira", sans-serif; font-weight: 500;
    font-size: 54px; line-height: 54px; letter-spacing: 6px;
    text-align: center; color: var(--ink);
  }

  .person {
    position: absolute; right: 29px; top: 218px; text-align: right;
    font-family: "Saira", sans-serif; font-weight: 400; color: var(--ink);
  }
  .person__name { font-size: 25px; line-height: 28px; }
  .person__title { font-size: 15px; line-height: 20px; margin-top: 2px; }

  .card--back .band { left: 128px; }
  .card--back .band--top { top: 0; height: 54px; }
  .card--back .band--bottom { top: 245px; bottom: 0; }

  .contacts { position: absolute; left: 128px; top: 61px; list-style: none; }
  .contact { display: flex; align-items: center; height: 38px; margin-bottom: 8px; }
  .contact__icon {
    width: 38px; height: 38px; background: var(--teal);
    display: flex; align-items: center; justify-content: center; flex: none;
  }
  .contact__text {
    margin-left: 7px; font-family: "Jura", sans-serif; font-weight: 500;
    color: var(--ink); white-space: nowrap;
  }
  .contact__text--small { font-size: 13px; }
  .contact__text--large { font-size: 17px; }
</style>
</head>
<body>
<main class="canvas">

  <section class="card card--front" aria-label="Business card front">
    <div class="band band--top"></div>
    <div class="band band--bottom"></div>
    <h1 class="brand-name">VELMORA</h1>
    <div class="person">
      <p class="person__name">Noam Ravid</p>
      <p class="person__title">Founder &amp; CEO</p>
    </div>
  </section>

  <section class="card card--back" aria-label="Business card back">
    <div class="band band--top"></div>
    <div class="band band--bottom"></div>
    <ul class="contacts">
      <li class="contact">
        <span class="contact__icon">
          <svg width="18" height="26" viewBox="0 0 18 26" aria-hidden="true">
            <rect x="2" y="1" width="14" height="24" rx="2.5" fill="none" stroke="#fff" stroke-width="2"/>
            <line x1="7" y1="21.5" x2="11" y2="21.5" stroke="#fff" stroke-width="1.6"/>
          </svg>
        </span>
        <span class="contact__text contact__text--small">+ 972-50-4417380</span>
      </li>
      <li class="contact">
        <span class="contact__icon">
          <svg width="28" height="26" viewBox="0 0 28 26" aria-hidden="true">
            <path d="M14 2 L26 13 L23 13 L23 24 L5 24 L5 13 L2 13 Z" fill="#fff"/>
            <rect x="11" y="15" width="6" height="6" fill="#0a8ca3"/>
          </svg>
        </span>
        <span class="contact__text contact__text--small">+ 972-73-6025514</span>
      </li>
      <li class="contact">
        <span class="contact__icon">
          <svg width="26" height="18" viewBox="0 0 26 18" aria-hidden="true">
            <rect x="1" y="1" width="24" height="16" fill="none" stroke="#fff" stroke-width="1.8"/>
            <path d="M1 1 L13 11 L25 1 M1 17 L10 8.5 M25 17 L16 8.5" fill="none" stroke="#fff" stroke-width="1.6"/>
          </svg>
        </span>
        <span class="contact__text contact__text--large">noam@velmora-studio.example</span>
      </li>
      <li class="contact">
        <span class="contact__icon">
          <svg width="26" height="26" viewBox="0 0 26 26" aria-hidden="true">
            <text x="13" y="20" text-anchor="middle" font-family="Saira, sans-serif" font-size="24" font-weight="500" fill="#fff">@</text>
          </svg>
        </span>
        <span class="contact__text contact__text--large">www.velmora-studio.example</span>
      </li>
    </ul>
  </section>

</main>
</body>
</html>
```